Amber Ridge Partners Business Card

A business card design to accompany the logo design you completed on Pixel Forum. We are open to your proposals. I did add one idea below that might work, but we aren't married to the idea. The company is a real estate services company. Clientele are typically high net worth individuals, executive level employment or owners of their own company, 30-60 years old.

Our 1 (bad?) idea: double sided card; One side landscape with logo and word mark. Other side Portrait with the logo only (oversize watermark maybe?). Somewhere add text of Name (Marcus Tellingham), Title (Principal), phone # (555-214-7736) and email address (marcus@amberridgeco.example). There would be a second design with my wife's name, number and email in place of mine.

Again totally open to ideas here.

Industry/Entity Type

Real Estate

```html
<!DOCTYPE html>
<html lang="en">
<head>
<meta charset="utf-8">
<title>Amber Ridge Partners — Business Cards</title>
<link rel="stylesheet" href="https://fonts.googleapis.com/css2?family=Open+Sans:wght@400;600&display=swap">
<style>
  :root {
    --bg: #efece6;
    --card-white: #ffffff;
    --band-grey: #7a7b7d;
    --band-grey-light: #a4a5a7;
    --sage: #4e8f45;
    --sage-back: #5f9a58;
    --text-dark: #3d3d3d;
    --text-mid: #6b6b6b;
    --shadow: rgba(0,0,0,0.18);
  }
  * { box-sizing: border-box; margin: 0; padding: 0; }
  html, body { width: 1200px; height: 508px; overflow: hidden; background: var(--bg); }
  body { font-family: "Open Sans", Arial, sans-serif; position: relative; }

  .card-set { position: absolute; top: 0; width: 600px; height: 508px; }
  .card-set--elena { left: 0; }
  .card-set--marcus { left: 600px; }

  .card { position: absolute; border-radius: 3px; box-shadow: 0 6px 16px var(--shadow); overflow: hidden; }

  .card-front { left: 40px; top: 70px; width: 340px; height: 194px; background: var(--card-white); }
  .card-front .band { position: absolute; inset: 0; width: 100%; height: 100%; }
  .card-front .web {
    position: absolute; left: 10px; bottom: 14px;
    transform-origin: left bottom; transform: rotate(-90deg) translate(0, 100%);
    color: #fff; font-size: 8px; font-weight: 600; letter-spacing: 0.2px;
  }
  .wordmark {
    position: absolute; left: 110px; top: 24px;
    display: flex; align-items: center; gap: 7px;
    color: var(--sage); font-size: 15px; font-weight: 400; letter-spacing: 1px; text-transform: uppercase; line-height: 1.15;
  }
  .wordmark .dot { width: 12px; height: 12px; border-radius: 50%; background: var(--sage); flex: none; }
  .person { position: absolute; right: 20px; top: 78px; text-align: right; }
  .person .name { font-size: 12px; font-weight: 600; color: var(--text-dark); }
  .person .title { font-size: 9px; color: var(--sage); margin-top: 1px; }
  .contact { position: absolute; right: 20px; top: 118px; text-align: right; font-size: 8px; color: var(--text-mid); line-height: 1.5; }
  .address { position: absolute; left: 110px; bottom: 16px; font-size: 8px; color: var(--text-mid); line-height: 1.5; }

  .card-back {
    left: 410px; top: 150px; width: 160px; height: 280px;
    background: linear-gradient(160deg, #6aa363 0%, var(--sage-back) 55%, #55904e 100%);
  }
  .card-back .web { position: absolute; right: 14px; bottom: 16px; color: #fff; font-size: 8px; font-weight: 600; }
</style>
</head>
<body>

<section class="card-set card-set--elena">
  <article class="card card-front">
    <svg class="band" viewBox="0 0 340 194" preserveAspectRatio="none" aria-hidden="true">
      <path d="M0 0 H78 C52 60 48 130 62 194 H0 Z" fill="var(--band-grey)"/>
      <path d="M78 0 C52 60 48 130 62 194" fill="none" stroke="var(--sage)" stroke-width="5"/>
      <path d="M86 0 C60 60 56 130 70 194" fill="none" stroke="var(--band-grey-light)" stroke-width="1"/>
    </svg>
    <span class="web">www.amberridgeco.example</span>
    <div class="wordmark"><span class="dot"></span><span>Amber Ridge<br>Partners</span></div>
    <div class="person">
      <p class="name">Elena Tellingham</p>
      <p class="title">Principal</p>
    </div>
    <div class="contact">
      <p>phone 555.214.7781</p>
      <p>elena@amberridgeco.example</p>
    </div>
    <div class="address">
      <p>418 Harbor Crest Way, Suite 310</p>
      <p>Bayview, CA 90000</p>
    </div>
  </article>
  <article class="card card-back">
    <span class="web">www.amberridgeco.example</span>
  </article>
</section>

<section class="card-set card-set--marcus">
  <article class="card card-front">
    <svg class="band" viewBox="0 0 340 194" preserveAspectRatio="none" aria-hidden="true">
      <path d="M0 0 H78 C52 60 48 130 62 194 H0 Z" fill="var(--band-grey)"/>
      <path d="M78 0 C52 60 48 130 62 194" fill="none" stroke="var(--sage)" stroke-width="5"/>
      <path d="M86 0 C60 60 56 130 70 194" fill="none" stroke="var(--band-grey-light)" stroke-width="1"/>
    </svg>
    <span class="web">www.amberridgeco.example</span>
    <div class="wordmark"><span class="dot"></span><span>Amber Ridge<br>Partners</span></div>
    <div class="person">
      <p class="name">Marcus Tellingham</p>
      <p class="title">Principal</p>
    </div>
    <div class="contact">
      <p>phone 555-214-7736</p>
      <p>marcus@amberridgeco.example</p>
    </div>
    <div class="address">
      <p>418 Harbor Crest Way, Suite 310</p>
      <p>Bayview, CA 90000</p>
    </div>
  </article>
  <article class="card card-back">
    <span class="web">www.amberridgeco.example</span>
  </article>
</section>

</body>
</html>
```